you will use Ai to Copy the website Wanderbay.com to come up with the basic frame work and it will give you the understanding of how I would like Coachlend.com to be like. Coachlend.com is a peer to peer rv rental site very similar to both of the other rv rental sites the difference is that are commission based 20% and above per rental and we will be one flat monthly rate and they keep all the earnings. Below is photo that will help you with the color scheme and the look and feel of the design

1 page

```html
<!DOCTYPE html>
<html lang="en">
<head>
<meta charset="utf-8">
<title>Coachlend.com – Peer-to-Peer RV Rentals</title>
<link href="https://fonts.googleapis.com/css2?family=Outfit:wght@400;500;600&family=Inter:wght@400;500;600&display=swap" rel="stylesheet">
<style>
:root{
  --green:#5b7a3a;
  --green-dark:#4a6630;
  --green-soft:#e6ebdc;
  --ink:#1e2420;
  --muted:#6b6f68;
  --line:#e2e0da;
  --bg:#f7f6f2;
  --card:#ffffff;
  --band:#ecebe5;
  --star:#e0a32a;
}
*{box-sizing:border-box;margin:0;padding:0}
html,body{width:800px;height:1200px;overflow:hidden;background:var(--bg)}
body{font-family:"Inter",sans-serif;color:var(--ink);font-size:9px;position:relative}
h1,h2,h3,.brand{font-family:"Outfit",sans-serif;font-weight:500}
.abs{position:absolute}
.btn{display:inline-flex;align-items:center;justify-content:center;background:var(--green);color:#fff;border-radius:5px;font-weight:500}

/* nav */
.nav{position:absolute;top:0;left:0;width:800px;height:62px;display:flex;align-items:center;padding:0 48px}
.brand{font-size:18px;font-weight:600;color:var(--ink);width:220px}
.nav-links{display:flex;gap:25px;font-size:9.5px;margin-left:45px}
.nav .btn{margin-left:auto;width:64px;height:27px;font-size:9.5px}

/* hero */
.hero-photo{top:62px;left:330px;width:470px;height:265px;background:linear-gradient(90deg,var(--bg) 0%,rgba(247,246,242,0) 28%),linear-gradient(180deg,#b9c4c7 0%,#8d9a94 35%,#6f8a93 55%,#55653f 78%,#7a7f76 100%)}
.hero-copy{top:86px;left:78px}
.hero-copy h1{font-size:36px;line-height:38px;letter-spacing:-.5px}
.hero-copy h1 span{color:var(--green)}
.hero-copy p{margin-top:20px;font-size:11px;line-height:17px}
.hero-actions{display:flex;align-items:center;gap:18px;margin-top:20px}
.hero-actions .btn{width:90px;height:29px;font-size:10px}
.play{display:flex;align-items:center;gap:9px;font-size:10px;font-weight:500}
.play i{width:24px;height:24px;border:1px solid #bbb;border-radius:50%;display:flex;align-items:center;justify-content:center;background:#fff}

/* search */
.tabs{top:275px;left:48px;display:flex}
.tab{width:143px;height:32px;display:flex;align-items:center;justify-content:center;gap:6px;font-size:10px;font-weight:500;background:#f1f0ec;border-radius:8px 8px 0 0;margin-right:1px}
.tab.on{background:var(--card);color:var(--green)}
.search{top:307px;left:48px;width:703px;height:82px;background:var(--card);border-radius:0 10px 10px 10px;box-shadow:0 4px 14px rgba(0,0,0,.05);padding:20px 18px;display:flex;gap:16px;align-items:flex-end}
.field label{display:block;font-size:9px;font-weight:500;margin-bottom:6px}
.input{height:27px;border:1px solid var(--line);border-radius:4px;display:flex;align-items:center;padding:0 8px;font-size:8.5px;color:#999;gap:5px;justify-content:space-between}
.search .btn{width:86px;height:29px;font-size:10px;margin-left:auto;margin-bottom:1px}

/* features */
.features{top:419px;left:50px;width:700px;display:flex;justify-content:space-between}
.feat{display:flex;gap:14px;width:170px}
.feat h3{font-family:"Inter",sans-serif;font-size:9.5px;font-weight:500;margin-bottom:6px}
.feat p{font-size:8px;line-height:13px;color:#444}

/* lifestyle */
.life-photo{top:483px;left:48px;width:345px;height:189px;border-radius:9px;background:linear-gradient(180deg,#c9b79a 0%,#7f7c6c 40%,#45503f 70%,#2a2e26 100%)}
.badge{top:575px;left:61px;width:65px;height:82px;background:rgba(91,122,58,.92);border-radius:7px;color:#fff;padding:14px 11px;text-align:center}
.badge b{font-family:"Outfit",sans-serif;font-size:20px;font-weight:500;display:block;margin-bottom:6px}
.badge span{font-size:8.5px;line-height:13px;display:block}
.life-copy{top:500px;left:422px}
.eyebrow{font-size:8.5px;font-weight:500;color:var(--green);letter-spacing:.3px}
.life-copy h2{font-size:24px;line-height:26px;margin:10px 0 16px}
.life-copy p{font-size:9.5px;line-height:15.5px;color:#333}
.life-copy .btn{margin-top:15px;width:80px;height:26px;font-size:9px}

/* popular */
.pop-head{top:699px;left:48px;width:703px}
.pop-head h2{font-size:18px;margin-top:6px}
.view-all{position:absolute;right:0;top:20px;font-size:9.5px;color:var(--green);font-weight:500}
.cards{top:746px;left:48px;width:703px;display:flex;gap:13px}
.card{flex:1;background:var(--card);border-radius:7px;overflow:hidden;box-shadow:0 2px 8px rgba(0,0,0,.05)}
.card-photo{height:87px;position:relative}
.card-photo i{position:absolute;right:9px;top:8px}
.card-body{padding:8px 8px 9px}
.card h3{font-family:"Inter",sans-serif;font-size:9px;font-weight:500}
.loc{font-size:7.5px;color:var(--muted);margin:3px 0 8px}
.specs{display:flex;gap:22px;font-size:7.5px;margin-bottom:13px}
.price{display:flex;justify-content:space-between;font-size:7.5px;color:var(--muted)}
.price b{font-size:9.5px;color:var(--ink);font-weight:600}
.price .rate{color:var(--ink)}
.price .rate em{color:var(--star);font-style:normal}

/* how it works */
.how{top:935px;left:0;width:800px;text-align:center}
.how h2{font-size:18px;margin-top:5px}
.steps{top:985px;left:86px;display:flex;align-items:center}
.step{display:flex;gap:12px;width:160px;text-align:left}
.step h3{font-family:"Inter",sans-serif;font-size:8px;font-weight:600;display:flex;gap:4px;align-items:center;margin-bottom:5px}
.step h3 span{width:10px;height:10px;border-radius:50%;background:var(--green);color:#fff;font-size:6.5px;display:inline-flex;align-items:center;justify-content:center}
.step p{font-size:7.5px;line-height:12px}
.dash{width:62px;border-top:1px dashed #bbb;margin:0 24px 0 0}

/* newsletter */
.news{top:1044px;left:0;width:800px;height:59px;background:var(--band);display:flex;align-items:center;padding:0 88px}
.mail{width:42px;height:42px;border-radius:50%;background:var(--green-soft);display:flex;align-items:center;justify-content:center}
.news h2{font-size:13px;line-height:16px;margin-left:15px}
.news .input{margin-left:auto;width:192px;height:26px;background:#fff;font-size:9px}
.news .btn{width:100px;height:27px;font-size:9.5px;margin-left:13px}

/* footer */
.footer{top:1103px;left:88px;width:624px;height:97px}
.footer .brand{font-size:14px;margin-top:10px;display:block}
.f-about{font-size:6.8px;line-height:11px;margin-top:6px;width:130px}
.social{display:flex;gap:12px;margin-top:8px}
.social i{width:12px;height:12px;border-radius:50%;background:var(--ink);display:block}
.f-col{position:absolute;top:14px}
.f-col h4{font-size:7px;font-weight:600;letter-spacing:.3px;margin-bottom:7px}
.f-col a{display:block;font-size:6.8px;line-height:11px;color:var(--ink);text-decoration:none}
.store{width:72px;height:22px;background:#111;border-radius:4px;margin-bottom:4px}
.copy{position:absolute;bottom:2px;left:0;width:624px;text-align:center;font-size:6.5px;color:#555}
</style>
</head>
<body>

<header class="nav">
  <div class="brand">Coachlend.com</div>
  <nav class="nav-links"><span>How It Works</span><span>List Your RV</span><span>Browse RVs</span><span>About Us</span><span>FAQs</span></nav>
  <span class="btn">Sign Up</span>
</header>

<div class="abs hero-photo" role="img" aria-label="Class C motorhome driving on a lakeside mountain road among pine trees"></div>
<section class="abs hero-copy">
  <h1>Rent. Explore.<br><span>Make Memories.</span></h1>
  <p>The peer-to-peer RV rental marketplace.<br>List it. Rent it. Bank it.</p>
  <div class="hero-actions">
    <span class="btn">Find an RV</span>
    <span class="play"><i><svg width="8" height="9" viewBox="0 0 8 9"><path d="M1 0.5 7.5 4.5 1 8.5z" fill="#1e2420"/></svg></i>How It Works</span>
  </div>
</section>

<div class="abs tabs">
  <div class="tab on"><svg width="11" height="11" viewBox="0 0 12 12" fill="none" stroke="currentColor" stroke-width="1.3"><circle cx="5" cy="5" r="4"/><path d="M8 8l3 3"/></svg>Find an RV</div>
  <div class="tab"><svg width="11" height="11" viewBox="0 0 12 12" fill="none" stroke="currentColor" stroke-width="1.2"><path d="M1 1h5l5 5-5 5-5-5z"/><circle cx="3.5" cy="3.5" r=".8"/></svg>List Your RV</div>
</div>
<form class="abs search">
  <div class="field" style="width:144px"><label>Pickup Location</label><div class="input" style="justify-content:flex-start"><svg width="8" height="9" viewBox="0 0 8 10" fill="none" stroke="#999"><path d="M4 9.5S7 6 7 4a3 3 0 0 0-6 0c0 2 3 5.5 3 5.5z"/></svg>Enter location</div></div>
  <div class="field" style="width:133px"><label>Pickup Date</label><div class="input">Select date<svg width="9" height="9" viewBox="0 0 10 10" fill="none" stroke="#999"><rect x=".5" y="1.5" width="9" height="8" rx="1"/><path d="M.5 4h9"/></svg></div></div>
  <div class="field" style="width:133px"><label>Return Date</label><div class="input">Select date<svg width="9" height="9" viewBox="0 0 10 10" fill="none" stroke="#999"><rect x=".5" y="1.5" width="9" height="8" rx="1"/><path d="M.5 4h9"/></svg></div></div>
  <div class="field" style="width:97px"><label>Guests</label><div class="input" style="color:var(--ink)">Any<svg width="8" height="5" viewBox="0 0 8 5" fill="none" stroke="#555"><path d="M1 1l3 3 3-3"/></svg></div></div>
  <span class="btn">Search</span>
</form>

<section class="abs features">
  <div class="feat"><svg width="30" height="26" viewBox="0 0 30 26" fill="none" stroke="var(--green)" stroke-width="1.4"><circle cx="15" cy="7" r="4"/><circle cx="6" cy="9" r="3"/><circle cx="24" cy="9" r="3"/><path d="M8 24c0-5 3-8 7-8s7 3 7 8M1 22c0-4 2-7 5-7M29 22c0-4-2-7-5-7"/></svg><div><h3>Peer-to-Peer</h3><p>Real people, real experiences</p></div></div>
  <div class="feat"><svg width="30" height="30" viewBox="0 0 30 30" fill="none" stroke="var(--green)" stroke-width="1.4"><circle cx="15" cy="15" r="13"/><path d="M10 20l10-10"/><circle cx="11" cy="11" r="1.8"/><circle cx="19" cy="19" r="1.8"/></svg><div><h3>20%+ Commission</h3><p>Earn more with every booking</p></div></div>
  <div class="feat"><svg width="28" height="26" viewBox="0 0 28 26" fill="none" stroke="var(--green)" stroke-width="1.4"><path d="M2 7h22v16H2zM2 7l16-5 2 5"/><path d="M18 13h8v5h-8z"/></svg><div><h3>One Flat Monthly Rate</h3><p>Keep all your earnings<br>with no hidden fees</p></div></div>
  <div class="feat"><svg width="26" height="30" viewBox="0 0 26 30" fill="none" stroke="var(--green)" stroke-width="1.4"><path d="M13 2l10 4v8c0 7-5 12-10 14C8 26 3 21 3 14V6z"/><path d="M8 15l4 4 6-7"/></svg><div><h3>Secure &amp; Insured</h3><p>Rent with confidence<br>and peace of mind</p></div></div>
</section>

<div class="abs life-photo" role="img" aria-label="Friends around a campfire beside a motorhome at a mountain lake at dusk"></div>
<div class="abs badge"><b>25+</b><span>Years of Adventure</span></div>
<section class="abs life-copy">
  <div class="eyebrow">THE RV LIFESTYLE</div>
  <h2>Where Roads<br>Lead to Memories.</h2>
  <p>From weekend getaways to cross-country<br>adventures — find the perfect RV and<br>experience the freedom of the open road.</p>
  <span class="btn">Explore RVs</span>
</section>

<section class="abs pop-head">
  <div class="eyebrow">POPULAR RVS</div>
  <h2>Top Picks for Your Next Adventure</h2>
  <span class="view-all">View all RVs &rarr;</span>
</section>
<div class="abs cards">
  <article class="card"><div class="card-photo" role="img" aria-label="Compact motorhome parked among pines with mountains" style="background:linear-gradient(180deg,#9fb0b8,#5f7450 55%,#3f4a36)"><i><svg width="13" height="12" viewBox="0 0 14 12" fill="none" stroke="#fff" stroke-width="1.3"><path d="M7 11S1 7 1 3.8A2.8 2.8 0 0 1 7 2.5a2.8 2.8 0 0 1 6 1.3C13 7 7 11 7 11z"/></svg></i></div>
    <div class="card-body"><h3>2022 Ridgeway Vista</h3><div class="loc">Denver, CO</div><div class="specs"><span>Sleeps 4</span><span>24 ft</span></div><div class="price"><span><b>$175</b> /night</span><span class="rate"><em>★</em> 4.9 <span style="color:var(--muted)">(28)</span></span></div></div></article>
  <article class="card"><div class="card-photo" role="img" aria-label="Travel trailer parked near a mountain meadow" style="background:linear-gradient(180deg,#a9bcc6,#6f8660 55%,#4a5a3e)"><i><svg width="13" height="12" viewBox="0 0 14 12" fill="none" stroke="#fff" stroke-width="1.3"><path d="M7 11S1 7 1 3.8A2.8 2.8 0 0 1 7 2.5a2.8 2.8 0 0 1 6 1.3C13 7 7 11 7 11z"/></svg></i></div>
    <div class="card-body"><h3>2021 Pinecrest Trail</h3><div class="loc">Boise, ID</div><div class="specs"><span>Sleeps 6</span><span>29 ft</span></div><div class="price"><span><b>$129</b> /night</span><span class="rate"><em>★</em> 4.8 <span style="color:var(--muted)">(19)</span></span></div></div></article>
  <article class="card"><div class="card-photo" role="img" aria-label="Fifth-wheel trailer at a campsite at sunset" style="background:linear-gradient(180deg,#d9a55e,#8a7458 50%,#3a3b30)"><i><svg width="13" height="12" viewBox="0 0 14 12" fill="none" stroke="#fff" stroke-width="1.3"><path d="M7 11S1 7 1 3.8A2.8 2.8 0 0 1 7 2.5a2.8 2.8 0 0 1 6 1.3C13 7 7 11 7 11z"/></svg></i></div>
    <div class="card-body"><h3>2023 Summit Horizon</h3><div class="loc">Portland, OR</div><div class="specs"><span>Sleeps 8</span><span>32 ft</span></div><div class="price"><span><b>$149</b> /night</span><span class="rate"><em>★</em> 5.0 <span style="color:var(--muted)">(35)</span></span></div></div></article>
  <article class="card"><div class="card-photo" role="img" aria-label="Class C motorhome on a lakeside road" style="background:linear-gradient(180deg,#b4c4ca,#7d9070 55%,#59674a)"><i><svg width="13" height="12" viewBox="0 0 14 12" fill="none" stroke="#fff" stroke-width="1.3"><path d="M7 11S1 7 1 3.8A2.8 2.8 0 0 1 7 2.5a2.8 2.8 0 0 1 6 1.3C13 7 7 11 7 11z"/></svg></i></div>
    <div class="card-body"><h3>2019 Northstar Elite</h3><div class="loc">San Diego, CA</div><div class="specs"><span>Sleeps 6</span><span>26 ft</span></div><div class="price"><span><b>$160</b> /night</span><span class="rate"><em>★</em> 4.7 <span style="color:var(--muted)">(22)</span></span></div></div></article>
</div>

<section class="abs how"><div class="eyebrow">HOW IT WORKS</div><h2>Renting Made Simple</h2></section>
<div class="abs steps">
  <div class="step"><svg width="40" height="38" viewBox="0 0 40 38" fill="none" stroke="var(--ink)" stroke-width="1.4"><circle cx="21" cy="18" r="9"/><path d="M14 25l-8 8"/><path d="M4 14a16 16 0 0 1 32 0" stroke="var(--green)"/></svg><div><h3><span>1</span>Find Your RV</h3><p>Search local RVs that fit<br>your trip and budget.</p></div></div>
  <div class="dash"></div>
  <div class="step" style="margin-left:4px"><svg width="36" height="38" viewBox="0 0 36 38" fill="none" stroke="var(--ink)" stroke-width="1.4"><rect x="2" y="5" width="28" height="28" rx="2"/><path d="M2 12h28M9 2v6M23 2v6M10 22l4 4 8-8"/><circle cx="29" cy="31" r="5" fill="var(--green)" stroke="none"/></svg><div><h3><span>2</span>Book &amp; Connect</h3><p>Book securely and connect<br>with the RV owner.</p></div></div>
  <div class="dash" style="margin-left:12px"></div>
  <div class="step"><svg width="38" height="34" viewBox="0 0 38 34" fill="none" stroke="var(--ink)" stroke-width="1.4"><path d="M2 32l11-18 8 12 5-7 10 13z"/><path d="M13 14l-3 7 3-2 3 2z" fill="var(--green)" stroke="none"/></svg><div><h3><span>3</span>Hit the Road</h3><p>Pick up, enjoy your trip,<br>and make memories!</p></div></div>
</div>

<section class="abs news">
  <div class="mail"><svg width="20" height="15" viewBox="0 0 20 15" fill="none" stroke="var(--green)" stroke-width="1.4"><rect x="1" y="1" width="18" height="13" rx="1"/><path d="M1 2l9 7 9-7"/></svg></div>
  <h2>Adventure Awaits.<br>Let's Go!</h2>
  <div class="input">Enter your email</div>
  <span class="btn">Subscribe</span>
</section>

<footer class="abs footer">
  <span class="brand">Coachlend.com</span>
  <p class="f-about">The peer-to-peer RV rental marketplace that helps you earn more and travel further.</p>
  <div class="social"><i></i><i></i><i></i></div>
  <div class="f-col" style="left:182px"><h4>COMPANY</h4><a>About Us</a><a>How It Works</a><a>List Your RV</a><a>Browse RVs</a><a>Blog</a></div>
  <div class="f-col" style="left:298px"><h4>SUPPORT</h4><a>FAQs</a><a>Safety</a><a>Insurance</a><a>Contact Us</a></div>
  <div class="f-col" style="left:406px"><h4>LEGAL</h4><a>Terms of Service</a><a>Privacy Policy</a></div>
  <div class="f-col" style="left:528px"><h4>DOWNLOAD THE APP</h4><div class="store"></div><div class="store"></div></div>
  <div class="copy">© 2025 Coachlend.com. All rights reserved.</div>
</footer>

</body>
</html>
```